wedding invitation card

Requirement:
1. White background, pink elements on the card, simple elegant looking
2. content:
Please join us as we celebrate new beginnings, new dreams,
and most importantly, new love at the marriage of
Miss Lin Qiao and Mr. Haoran Bei
Friday, The First of January
Two Thousand Fifteen at Eleven o’clock
Coral Breeze Hotel Palm Garden Deck.

Reception will be followed at Lantern Hall at Half-Past Twelve o'clock

Please RSVP before December 18th 2015 by email: qiaolin0317@mailnest.example

3. Flat paper
4. be able to change the size of the design according to printing requirement

```html
<!DOCTYPE html>
<html lang="en">
<head>
<meta charset="utf-8">
<title>Wedding Invitation – Lin Qiao &amp; Haoran Bei</title>
<link rel="stylesheet" href="https://fonts.googleapis.com/css2?family=Pinyon+Script&family=Cormorant+Garamond:ital,wght@1,400&family=Nunito+Sans:wght@300&display=swap">
<style>
  :root {
    --board: #d6d6d6;
    --paper: #ffffff;
    --plum: #4a0d2c;
    --rose: #a3145e;
    --ink: #111111;
    --info: #5a5a5a;
    --rule: #8a8a8a;
    --label: #ffffff;
    --bloom-pink: #e58bb3;
    --bloom-coral: #ef8f8a;
    --bloom-violet: #9a78c0;
    --bloom-leaf: #8fcdb8;
  }
  * { margin: 0; padding: 0; box-sizing: border-box; }
  html, body { width: 1200px; height: 760px; overflow: hidden; background: var(--board); }
  .board { position: relative; width: 1200px; height: 760px; }

  .card { position: absolute; background: var(--paper); }
  .card--front { left: 64px; top: 96px; width: 512px; height: 256px; }
  .card--back  { left: 70px; top: 398px; width: 512px; height: 256px; outline: 1px solid #222; }
  .card--open  { left: 615px; top: 65px; width: 512px; height: 512px; }
  .card--open .fold { position: absolute; left: 0; right: 0; top: 256px; height: 1px; background: #ececec; }

  .label {
    position: absolute;
    font-family: "Cormorant Garamond", serif;
    font-style: italic;
    font-size: 18px;
    color: var(--label);
  }
  .label--front { left: 72px; top: 356px; }
  .label--back  { left: 96px; top: 660px; }
  .label--open  { left: 619px; top: 600px; }

  .bloom { position: absolute; border-radius: 46% 54% 50% 50%; }
  .bloom--front {
    left: 232px; top: 4px; width: 264px; height: 244px;
    background: radial-gradient(circle at 40% 30%, var(--bloom-pink) 0%, transparent 45%),
                radial-gradient(circle at 62% 55%, var(--bloom-coral) 0%, transparent 45%),
                radial-gradient(circle at 20% 25%, var(--bloom-violet) 0%, transparent 30%),
                radial-gradient(circle at 30% 85%, var(--bloom-leaf) 0%, transparent 35%),
                #fbe9ef;
    opacity: .9;
  }
  .bloom--back {
    left: 194px; top: 82px; width: 124px; height: 76px;
    background: radial-gradient(circle at 30% 40%, var(--bloom-coral) 0%, transparent 55%),
                radial-gradient(circle at 75% 25%, var(--bloom-violet) 0%, transparent 40%),
                radial-gradient(circle at 75% 80%, var(--bloom-leaf) 0%, transparent 40%),
                #fbeeee;
  }

  .title {
    position: absolute; left: 140px; top: 150px;
    font-family: "Pinyon Script", cursive;
    font-size: 54px; color: var(--plum);
  }
  .date {
    position: absolute; left: 0; right: 0; top: 158px; text-align: center;
    font-family: "Cormorant Garamond", serif; font-style: italic;
    font-size: 11px; color: #555;
  }

  .vows { position: absolute; left: 0; top: 0; }
  .script { font-family: "Pinyon Script", cursive; }
  .details {
    position: absolute; top: 440px; left: 44px; right: 24px;
    display: flex;
    font-family: "Nunito Sans", sans-serif; font-weight: 300;
    font-size: 7.6px; line-height: 9.6px; color: var(--info);
  }
  .details__col { padding: 0 0 6px 0; }
  .details__col--when  { width: 103px; }
  .details__col--where { width: 192px; padding-left: 18px; border-left: 1px solid var(--rule); }
  .details__col--rsvp  { padding-left: 11px; border-left: 1px solid var(--rule); }
  .details__col p + p { margin-top: 9.6px; }
</style>
</head>
<body>
<main class="board">

  <section class="card card--front">
    <div class="bloom bloom--front" role="img" aria-label="Watercolour bouquet of pink, coral and violet flowers with teal leaves"></div>
    <h1 class="title">Invitation</h1>
  </section>
  <p class="label label--front">front (200 x 100 mm)</p>

  <section class="card card--back">
    <div class="bloom bloom--back" role="img" aria-label="Small watercolour coral rose with violet buds and a leaf"></div>
    <p class="date">1.01.2016</p>
  </section>
  <p class="label label--back">back</p>

  <section class="card card--open">
    <div class="fold"></div>
    <svg class="vows" width="512" height="512" viewBox="0 0 512 512">
      <defs>
        <path id="arc-one" d="M100 320 Q240 270 385 302"/>
        <path id="arc-two" d="M176 320 Q300 300 420 336"/>
      </defs>
      <text class="script" font-size="14" fill="var(--ink)"><textPath href="#arc-one">Please join us as we celebrate new beginnings, new dreams,</textPath></text>
      <text class="script" font-size="14" fill="var(--ink)"><textPath href="#arc-two">and most importantly, new love at the marriage of</textPath></text>

      <text class="script" x="150" y="354" font-size="24" fill="var(--ink)">miss</text>
      <text class="script" x="194" y="354" font-size="46" fill="var(--rose)">Lin</text>
      <text class="script" x="264" y="354" font-size="46" fill="var(--ink)">Qiao</text>
      <text class="script" x="228" y="372" font-size="22" fill="var(--ink)">and</text>
      <text class="script" x="143" y="396" font-size="24" fill="var(--ink)">mr.</text>
      <text class="script" x="184" y="396" font-size="46" fill="var(--ink)">Haoran Bei</text>
    </svg>

    <div class="details">
      <div class="details__col details__col--when">
        FRIDAY,<br>THE FIRST OF JANUARY<br>Two Thousand Fifteen<br>at Eleven o'clock
      </div>
      <div class="details__col details__col--where">
        <p>Coral Breeze Hotel Palm Garden Deck.</p>
        <p>Reception will be followed<br>at Lantern Hall at Half-Past Twelve o'clock</p>
      </div>
      <div class="details__col details__col--rsvp">
        Please RSVP<br>before December 18th 2015<br>by email: qiaolin0317@mailnest.example
      </div>
    </div>
  </section>
  <p class="label label--open">open (200 x 200 mm)</p>

</main>
</body>
</html>
```